Powerpoint and Word template required

We need PowerPoint and Word templates for all of our company branded materials and stationary. We have recently rebranded our website and would like something that is reflective of our new corporate branding. A sample of some of the documents we have created recently are attached and our website is below

http://lorventamedical.com.au/

The word template will be used for all letters we send to clients and customers and we think we want the logo and ISO 9001 cert to only appear on the first page.

The powerpoint template has to be flexible as we use this for both marketing and training purposes. I have attached a couple of samples of the types of documents we create and note that these are very basic / crude and we would be looking for something that is a significant improvement on these

In the powerpoint template it would be good to have lots of standard layouts within the template, e.g. different 'standard layouts for multiple elements on a page including pictures and text etc.
Updates

Project Deadline Extended
Reason: Still looking for a professional yet modern template and important to us that we can see more tan just a title slide and the layout of the other slide master slides is very important to us. Many thanks, Doug

Industry/Entity Type

Healthcare

Font styles to use
Sans Serif

Colors
33a6d7

Requirements
Must have
• Templates must be versatile for use; powerpoint template must be able to be used for training materials and weel as marketing / pitch books.
• Word template must be able to be used as a basis for our corporate letter head through to RFP response type documents as well as Reference / Operating manual type of documents
• In terms of the design it must be consistent with our new corporate image which is best represented by our new website design; www.lorventamedical.com

```html
<!DOCTYPE html>
<html lang="en">
<head>
<meta charset="utf-8">
<title>Lorventa – Presentation Layouts</title>
<link href="https://fonts.googleapis.com/css2?family=Bebas+Neue&family=Raleway:wght@400;500;700&display=swap" rel="stylesheet">
<style>
  :root{
    --navy:#1b5597;
    --blue:#2a72bb;
    --mid:#4a8cd0;
    --sky:#8fbbe6;
    --mist:#d6e6f6;
    --pale:#f4f8fd;
    --ink:#4a525c;
    --list-ink:#263445;
    --white:#ffffff;
    --frame:#111111;
    --panel:rgba(140,185,232,.55);
  }
  *{margin:0;padding:0;box-sizing:border-box}
  html,body{width:990px;height:1200px;overflow:hidden;background:var(--white)}
  body{position:relative;font-family:"Raleway",sans-serif;color:var(--ink)}

  .slide{position:absolute;width:430px;height:243px;border:2px solid var(--frame);overflow:hidden;background:var(--white)}
  .col-left{left:50px}.col-right{left:513px}
  .row-1{top:40px}.row-2{top:326px}.row-3{top:625px}.row-4{top:921px}

  .art{position:absolute;inset:0}
  .art-deep{background:linear-gradient(160deg,var(--navy) 0%,var(--blue) 55%,var(--mid) 100%)}
  .art-title{background:linear-gradient(166deg,var(--navy) 0%,var(--mid) 20%,var(--mist) 42%,var(--pale) 65%,var(--white) 100%)}
  .art-section{background:linear-gradient(172deg,var(--navy) 0%,var(--blue) 40%,var(--sky) 62%,var(--pale) 82%)}
  .art-two{background:linear-gradient(180deg,var(--navy) 0,var(--blue) 40px,var(--mist) 62px,var(--pale) 120px,var(--white) 100%)}
  .art-corners{background:
      radial-gradient(ellipse 150px 110px at 0 0,var(--navy) 0%,var(--mid) 45%,rgba(143,187,230,0) 100%),
      radial-gradient(ellipse 140px 110px at 100% 100%,var(--navy) 0%,var(--mid) 45%,rgba(143,187,230,0) 100%),
      linear-gradient(180deg,var(--white),var(--pale))}

  .band{position:absolute;left:0;right:0;top:76px;height:90px;background:var(--white)}
  .rule{position:absolute;left:0;right:0;top:185px;height:1px;background:var(--sky)}
  .panel{position:absolute;top:61px;bottom:0;background:var(--panel)}

  .heading{position:absolute;font-family:"Bebas Neue",sans-serif;line-height:1;letter-spacing:3px}
  .heading.light{color:var(--white)}
  .heading.dark{color:var(--blue)}

  .brand-box{position:absolute;left:78px;top:65px;width:269px;height:111px;background:var(--white);display:flex;align-items:center;gap:14px;padding-left:22px}
  .brand-mark{width:55px;height:55px;background:var(--blue);border-radius:4px}
  .brand-name{font-weight:700;font-size:42px;color:var(--blue);letter-spacing:-.5px}

  .body-copy{position:absolute;left:45px;top:65px;font-size:10.3px;line-height:17px;letter-spacing:.7px;white-space:nowrap}
  .small-copy{position:absolute;top:56px;font-size:6.3px;line-height:12.4px;letter-spacing:.35px;white-space:nowrap;color:#3d4550}
  .small-copy p+p{margin-top:12.4px}
  .side-copy{position:absolute;left:215px;top:58px;font-size:7.6px;line-height:12.4px;letter-spacing:.4px;white-space:nowrap}
  .side-copy p+p{margin-top:12.4px}
  .sub-text{position:absolute;left:24px;top:198px;font-size:14px;letter-spacing:1.5px}

  .list{position:absolute;top:78px;list-style:none;font-size:5.9px;letter-spacing:.35px;color:var(--list-ink);white-space:nowrap}
  .list li{height:28px}

  .placeholder{position:absolute;left:57px;top:60px;width:120px;height:120px;border:1.6px solid var(--frame)}
  .placeholder svg{position:absolute;inset:0;width:100%;height:100%}
  .placeholder span{position:absolute;left:0;right:0;top:16px;text-align:center;font-size:11px;font-weight:700;letter-spacing:1.2px;color:var(--frame)}
</style>
</head>
<body>

<section class="slide col-left row-1">
  <div class="art art-deep" role="img" aria-label="Flowing blue wave background"></div>
  <div class="band"></div>
  <div class="brand-box">
    <div class="brand-mark"></div>
    <div class="brand-name">Lorventa</div>
  </div>
</section>

<section class="slide col-right row-1">
  <div class="art art-title" role="img" aria-label="Blue wave sweeping from the top left"></div>
  <div class="rule"></div>
  <div class="heading light" style="left:45px;top:19px;font-size:30px">Title</div>
  <div class="body-copy">
    Lorem ipsum dolor sit amet, consectetur adipiscing elit.<br>
    Vivamus sit amet urna non massa sagittis suscipit quis sed libero.<br>
    Nullam ultricies nisi at risus pretium laoreet sit amet sit amet eros.<br>
    Nam feugiat nisi id tortor consectetur, a bibendum dolor pharetra.<br>
    Cras placerat nisi et luctus lacinia.<br>
    In viverra nibh sed neque fringilla, vitae gravida diam hendrerit.<br>
    Vivamus sollicitudin mi eget dui dignissim dignissim.<br>
    Fusce dignissim massa a odio eleifend placerat.
  </div>
</section>

<section class="slide col-left row-2">
  <div class="art art-section" role="img" aria-label="Large blue wave across the upper slide"></div>
  <div class="heading dark" style="left:25px;top:163px;font-size:30px">Section Header</div>
  <div class="sub-text">SUB TEXT</div>
</section>

<section class="slide col-right row-2">
  <div class="art art-two" role="img" aria-label="Blue wave band along the top"></div>
  <div class="heading light" style="left:27px;top:9px;font-size:28px;letter-spacing:3.5px">Two Contents</div>
  <div class="small-copy" style="left:26px">
    <p>Lorem ipsum dolor sit amet, consectetuer adipisc-<br>ing elit. Donec odio. Quisque volutpat mattis eros.<br>Nullam malesuada erat ut turpis. Suspendisse urna<br>nibh, viverra non, semper suscipit, posuere a, pede.</p>
    <p>Donec nec justo eget felis facilisis fermentum.<br>Aliquam porttitor mauris sit amet orci. Aenean<br>dignissim pellentesque felis.</p>
    <p>Morbi in sem quis dui placerat ornare. Pellentesque<br>odio nisi, euismod in, pharetra a, ultricies in, diam.<br>Sed arcu. Cras consequat.</p>
  </div>
  <div class="small-copy" style="left:232px">
    <p>Lorem ipsum dolor sit amet, consectetuer adipisc-<br>ing elit. Donec odio. Quisque volutpat mattis eros.<br>Nullam malesuada erat ut turpis. Suspendisse urna<br>nibh, viverra non, semper suscipit, posuere a, pede.</p>
    <p>Donec nec justo eget felis facilisis fermentum.<br>Aliquam porttitor mauris sit amet orci. Aenean<br>dignissim pellentesque felis.</p>
    <p>Morbi in sem quis dui placerat ornare. Pellentesque<br>odio nisi, euismod in, pharetra a, ultricies in, diam.<br>Sed arcu. Cras consequat.</p>
  </div>
</section>

<section class="slide col-left row-3">
  <div class="art art-deep" role="img" aria-label="Flowing blue wave background"></div>
  <div class="panel" style="left:0;width:212px"></div>
  <div class="panel" style="left:217px;right:0"></div>
  <div class="heading light" style="left:0;right:0;top:21px;text-align:center;font-size:30px">Comparison</div>
  <ol class="list" style="left:11px">
    <li>1. Lorem ipsum dolor sit amet, consectetuer adipiscing elit.</li>
    <li>2. Aliquam tincidunt mauris eu risus.</li>
    <li>3. Vestibulum auctor dapibus neque.</li>
    <li>4. Nunc dignissim risus id metus.</li>
    <li>5. Cras ornare tristique elit.</li>
  </ol>
  <ol class="list" style="left:226px">
    <li>1. Lorem ipsum dolor sit amet, consectetuer adipiscing elit.</li>
    <li>2. Aliquam tincidunt mauris eu risus.</li>
    <li>3. Vestibulum auctor dapibus neque.</li>
    <li>4. Nunc dignissim risus id metus.</li>
    <li>5. Cras ornare tristique elit.</li>
  </ol>
</section>

<section class="slide col-right row-3">
  <div class="art art-deep" role="img" aria-label="Flowing blue wave background"></div>
  <div class="heading light" style="left:0;right:0;top:102px;text-align:center;font-size:30px">Blank</div>
</section>

<section class="slide col-left row-4">
  <div class="art art-corners" role="img" aria-label="Blue wave accents in the top left and bottom right corners"></div>
  <div class="placeholder">
    <svg viewBox="0 0 120 120" preserveAspectRatio="none">
      <line x1="0" y1="0" x2="120" y2="120" stroke="#111" stroke-width="1.2"/>
      <line x1="120" y1="0" x2="0" y2="120" stroke="#111" stroke-width="1.2"/>
    </svg>
    <span>IMAGE</span>
  </div>
  <div class="side-copy">
    <p>Lorem ipsum dolor sit amet, consectetuer<br>adipiscing elit. Donec odio. Quisque volut-<br>pat mattis eros. Nullam malesuada erat ut<br>turpis. Suspendisse urna nibh, viverra non,<br>semper suscipit, posuere a, pede.</p>
    <p>Donec nec justo eget felis facilisis fermen-<br>tum. Aliquam porttitor mauris sit amet orci.<br>Aenean dignissim pellentesque felis.</p>
  </div>
</section>

<section class="slide col-right row-4">
  <div class="art art-corners" role="img" aria-label="Blue wave accents in the top left and bottom right corners"></div>
  <div class="heading dark" style="left:27px;top:103px;font-size:42px;letter-spacing:4.5px">Content</div>
  <div class="side-copy">
    <p>Lorem ipsum dolor sit amet, consectetuer<br>adipiscing elit. Donec odio. Quisque volut-<br>pat mattis eros. Nullam malesuada erat ut<br>turpis. Suspendisse urna nibh, viverra non,<br>semper suscipit, posuere a, pede.</p>
    <p>Donec nec justo eget felis facilisis fermen-<br>tum. Aliquam porttitor mauris sit amet orci.<br>Aenean dignissim pellentesque felis.</p>
  </div>
</section>

</body>
</html>
```